Business Card Design for Property Development Company Director

I am looking for a professional and unforgettable business card design for our Director of our Property Development Company.
Please see attached .pptx file to find out what information to include. You don't have to follow the exact format shown in the file - I am interested to see your creative flair using the information provided.

```html
<!DOCTYPE html>
<html lang="en">
<head>
<meta charset="utf-8">
<title>Norvale Property Group – Business Card</title>
<link href="https://fonts.googleapis.com/css2?family=Lato:ital,wght@0,400;0,700;1,400&family=Open+Sans:wght@600&display=swap" rel="stylesheet">
<style>
  :root {
    --brand-blue: #1059a8;
    --accent-blue: #1a6fc0;
    --brand-grey: #57585a;
    --text-dark: #333333;
    --card-white: #ffffff;
    --stage: #e8e5e0;
  }
  * { margin: 0; padding: 0; box-sizing: border-box; }
  html, body { width: 900px; height: 1200px; overflow: hidden; }
  body {
    position: relative;
    background: var(--stage);
    font-family: "Lato", Arial, sans-serif;
  }
  .card {
    position: absolute;
    left: 86px;
    width: 735px;
    height: 430px;
    overflow: hidden;
    box-shadow: 0 6px 14px rgba(0,0,0,0.18);
  }
  .card-front { top: 137px; background: var(--card-white); }
  .card-back { top: 633px; background: var(--brand-blue); }

  .wordmark { position: absolute; display: flex; align-items: center; }
  .wordmark-square { background: currentColor; flex: none; }
  .wordmark-text { font-family: "Lato", Arial, sans-serif; font-weight: 700; line-height: 1; }
  .wordmark-name { display: block; letter-spacing: 0.5px; }
  .wordmark-sub { display: block; letter-spacing: 3.2px; }

  .front-mark { top: 54px; right: 52px; color: var(--brand-blue); gap: 18px; }
  .front-mark .wordmark-square { width: 78px; height: 78px; }
  .front-mark .wordmark-name { font-size: 50px; }
  .front-mark .wordmark-sub { font-size: 18px; margin-top: 6px; }

  .faint-square {
    position: absolute;
    left: 492px; top: 224px;
    width: 170px; height: 140px;
    background: var(--brand-blue);
    opacity: 0.04;
  }

  .person { position: absolute; left: 52px; top: 225px; }
  .person-name { font-weight: 700; font-size: 27px; color: var(--brand-blue); letter-spacing: -0.2px; }
  .person-role { font-size: 17px; color: var(--text-dark); margin-top: 3px; }

  .contact-list { position: absolute; left: 52px; top: 303px; list-style: none; }
  .contact-list li {
    display: flex; align-items: center; gap: 10px;
    font-size: 17.5px; color: var(--text-dark);
    height: 29px;
  }
  .contact-list svg { width: 13px; height: 13px; fill: var(--brand-blue); flex: none; }

  .licence {
    position: absolute; right: 53px; top: 361px;
    font-size: 15px; color: var(--text-dark);
  }
  .licence-label { color: var(--brand-blue); }

  .front-band-blue { position: absolute; left: 0; bottom: 0; width: 416px; height: 15px; background: var(--accent-blue); }
  .front-band-grey { position: absolute; right: 0; bottom: 0; width: 313px; height: 15px; background: #4a4b4d; }

  .tagline {
    position: absolute; top: 56px; left: 0; width: 100%;
    text-align: center;
    font-family: "Open Sans", Arial, sans-serif; font-weight: 600;
    font-size: 22px; line-height: 30px; color: var(--card-white);
    letter-spacing: 0.3px;
  }
  .back-faint-square {
    position: absolute; left: 380px; top: 128px;
    width: 250px; height: 230px;
    background: var(--card-white); opacity: 0.05;
  }
  .back-mark { top: 175px; left: 108px; color: var(--card-white); gap: 26px; }
  .back-mark .wordmark-square { width: 118px; height: 118px; }
  .back-mark .wordmark-name { font-size: 72px; }
  .back-mark .wordmark-sub { font-size: 25px; margin-top: 8px; letter-spacing: 4.4px; }

  .offer {
    position: absolute; top: 370px; left: 0; width: 100%;
    text-align: center; font-style: italic;
    font-size: 17.5px; color: var(--card-white);
  }
</style>
</head>
<body>

<section class="card card-front" aria-label="Business card front">
  <div class="wordmark front-mark">
    <span class="wordmark-square"></span>
    <span class="wordmark-text">
      <span class="wordmark-name">NORVALE</span>
      <span class="wordmark-sub">PROPERTY GROUP</span>
    </span>
  </div>

  <div class="faint-square"></div>

  <div class="person">
    <h1 class="person-name">DANIEL ASHFORD</h1>
    <p class="person-role">Director</p>
  </div>

  <ul class="contact-list">
    <li>
      <svg viewBox="0 0 24 24" aria-hidden="true"><path d="M6.6 10.8a15.1 15.1 0 0 0 6.6 6.6l2.2-2.2a1 1 0 0 1 1-.25 11.4 11.4 0 0 0 3.6.57 1 1 0 0 1 1 1V20a1 1 0 0 1-1 1A17 17 0 0 1 3 4a1 1 0 0 1 1-1h3.5a1 1 0 0 1 1 1c0 1.25.2 2.45.57 3.6a1 1 0 0 1-.25 1z"/></svg>
      0400 318 265
    </li>
    <li>
      <svg viewBox="0 0 24 24" aria-hidden="true"><path d="M2 5h20v2.2l-10 6.3L2 7.2z"/><path d="M2 9.6l10 6.3 10-6.3V19H2z"/></svg>
      daniel@norvale.com.au
    </li>
    <li>
      <svg viewBox="0 0 24 24" aria-hidden="true"><path d="M12 2a10 10 0 1 0 0 20 10 10 0 0 0 0-20zm6.9 6h-2.9a15 15 0 0 0-1.4-3.6A8 8 0 0 1 18.9 8zM12 4c.8 1.2 1.5 2.5 1.9 4h-3.8c.4-1.5 1.1-2.8 1.9-4zM4.3 14a8 8 0 0 1 0-4h3.4a16 16 0 0 0 0 4zm.8 2h2.9c.3 1.3.8 2.5 1.4 3.6A8 8 0 0 1 5.1 16zM8 8H5.1a8 8 0 0 1 4.3-3.6C8.8 5.5 8.3 6.7 8 8zm4 12c-.8-1.2-1.5-2.5-1.9-4h3.8c-.4 1.5-1.1 2.8-1.9 4zm2.3-6H9.7a14 14 0 0 1 0-4h4.6a14 14 0 0 1 0 4zm.3 5.6c.6-1.1 1.1-2.3 1.4-3.6h2.9a8 8 0 0 1-4.3 3.6zm1.7-5.6a16 16 0 0 0 0-4h3.4a8 8 0 0 1 0 4z"/></svg>
      www.norvale.com.au
    </li>
  </ul>

  <p class="licence"><span class="licence-label">Real Estate Lic:</span> 5172036 &amp; 5172037</p>

  <div class="front-band-blue"></div>
  <div class="front-band-grey"></div>
</section>

<section class="card card-back" aria-label="Business card back">
  <p class="tagline">Property Development<br>&amp; Site Acquisition Specialists</p>
  <div class="back-faint-square"></div>
  <div class="wordmark back-mark">
    <span class="wordmark-square"></span>
    <span class="wordmark-text">
      <span class="wordmark-name">NORVALE</span>
      <span class="wordmark-sub">PROPERTY GROUP</span>
    </span>
  </div>
  <p class="offer">Ask me about our INVESTMENT &amp; PARTNERSHIP opportunities</p>
</section>

</body>
</html>
```